Domestic Building Company requires professional webpage

We have an existing webpage that was never completed. We are a growing building company specialising in domestic building, renovations and commercial maintenance. We liaise closely with each of our clients to provide quality service they would be happy to recommend. Our easy approachable staff give our clients the confidence to discuss their needs and changes they may have along the way.
Our main source of new customers have been from recommendations of existing clients.
We would like our webpage to reflect our eye for detail and showcase our previous work.
The colour theme should be the same as the colours of our logo.
We would like the main page to really stand out with a slideshow of our pictures of works we have completed.
We would like the tabs to remain the same - Home, About Us, Our Services, Contact us.
In the Our Services section we would like each sub heading to be a link where viewers can see pictures from previous work we have completed.
Our current web page is www.ferncastconstruct.com.au

```html
<!DOCTYPE html>
<html lang="en">
<head>
<meta charset="utf-8">
<title>Ferncast Construct – Home</title>
<link rel="stylesheet" href="https://fonts.googleapis.com/css2?family=Source+Sans+3:wght@300;400&display=swap">
<style>
  :root {
    --brand-green: #7cc553;
    --brand-blue: #2b6cb3;
    --header-bg: #ffffff;
    --nav-text: #6a6a6a;
    --panel-bg: rgba(255, 255, 255, 0.9);
    --panel-heading: #2a2a2a;
    --panel-text: #333333;
    --footer-bg: rgba(20, 20, 20, 0.72);
    --footer-text: #f2f2f2;
  }
  * { box-sizing: border-box; margin: 0; padding: 0; }
  html, body {
    width: 1200px;
    height: 668px;
    overflow: hidden;
    font-family: "Source Sans 3", "Helvetica Neue", Arial, sans-serif;
    background: #ffffff;
  }
  .page {
    position: relative;
    width: 1200px;
    height: 668px;
    overflow: hidden;
  }
  .site-header {
    position: absolute;
    top: 0; left: 0;
    width: 1200px;
    height: 79px;
    background: var(--header-bg);
  }
  .brand {
    position: absolute;
    left: 150px;
    top: 22px;
    display: flex;
    align-items: center;
    gap: 10px;
  }
  .brand-square {
    width: 30px;
    height: 30px;
    background: var(--brand-green);
  }
  .brand-name {
    font-size: 28px;
    font-weight: 400;
    color: var(--brand-blue);
    letter-spacing: 0.5px;
    line-height: 1;
  }
  .main-nav {
    position: absolute;
    top: 0;
    left: 767px;
    height: 79px;
    display: flex;
    list-style: none;
  }
  .main-nav a {
    display: block;
    height: 79px;
    line-height: 83px;
    padding: 0 11px;
    font-size: 13.5px;
    font-weight: 300;
    color: var(--nav-text);
    text-decoration: none;
  }
  .main-nav .is-active a {
    background: var(--brand-green);
    color: #ffffff;
  }
  .hero-photo {
    position: absolute;
    top: 79px; left: 0;
    width: 1200px;
    height: 589px;
    background:
      radial-gradient(ellipse 260px 120px at 120px 40px, rgba(210, 222, 230, 0.85), transparent 70%),
      linear-gradient(180deg, transparent 60%, rgba(90, 70, 50, 0.55) 100%),
      linear-gradient(90deg, #5d7a3e 0%, #4d6a34 22%, #6c6a52 36%, #3e3a34 48%, #2f2d2a 70%, #3a3631 100%);
  }
  .welcome-panel {
    position: absolute;
    left: 515px;
    top: 263px;
    width: 535px;
    height: 207px;
    background: var(--panel-bg);
    border-radius: 3px;
    padding: 16px 18px 0 18px;
  }
  .welcome-panel h1 {
    font-size: 27px;
    font-weight: 300;
    color: var(--panel-heading);
    line-height: 1.2;
    margin-bottom: 8px;
  }
  .welcome-panel p {
    font-size: 13.3px;
    font-weight: 300;
    line-height: 18.7px;
    color: var(--panel-text);
  }
  .site-footer {
    position: absolute;
    left: 0;
    bottom: 0;
    width: 1200px;
    height: 40px;
    background: var(--footer-bg);
  }
  .site-footer p {
    position: absolute;
    left: 150px;
    top: 12px;
    font-size: 11.3px;
    font-weight: 300;
    color: var(--footer-text);
  }
</style>
</head>
<body>
<div class="page">
  <header class="site-header">
    <div class="brand">
      <span class="brand-square"></span>
      <span class="brand-name">ferncast</span>
    </div>
    <ul class="main-nav">
      <li class="is-active"><a href="#">home</a></li>
      <li><a href="#">about us</a></li>
      <li><a href="#">our services</a></li>
      <li><a href="#">contact us</a></li>
    </ul>
  </header>

  <div class="hero-photo" role="img" aria-label="Slideshow photo of a completed timber deck with a covered pergola, glass balustrade, outdoor chairs and trees behind"></div>

  <section class="welcome-panel">
    <h1>Welcome to Ferncast</h1>
    <p>Ferncast Construct Pty Ltd is a construction and renovation company that is based in the Illawarra area.&nbsp; We specialise in all areas of residential and commercial building works and aim to deliver the highest quality performance at an affordable price. We ensure our workers have undergone the qualifications and training to provide the workmanship, efficiency and reliability our clients expect. We actively engage our client from the initial greeting to the finished product, we achieve this by ensuring the clients needs remain our first priority when delivering a high quality service and product.</p>
  </section>

  <footer class="site-footer">
    <p>Copyright 2014 Ferncast Construct Pty Ltd | ABN: 48 615 203 917 | Lic: 204816B</p>
  </footer>
</div>
</body>
</html>
```